Crumb Joy pastry business card design

I need a logo and a business card design for my baking business, "Crumb Joy". I daily bake French pastries from scratch using high quality ingredients and directly cater to local customers. My product is very authentic but sold at a casual setting . I'm looking for a simple, cute, stylish yet earthy design. Like this kind of feel:
http://clipvista.example/71946302
Target Market(s)
Metropolitan food conscious consumers in their 20-40s
Industry/Entity Type
Business
Requirements
Must have
- Soft pastel colors or other types of color schemes that would remind French pastries.
email: welovecrumbles@mailnest.example
twitter@bitemesf
www.crumbjoyla.example
Nice to have
Should not have
- pictures of pastries - sketches are ok.

```html
<!DOCTYPE html>
<html lang="en">
<head>
<meta charset="utf-8">
<title>Crumb Joy – Business Card</title>
<link rel="stylesheet" href="https://fonts.googleapis.com/css2?family=Great+Vibes&family=Tinos&display=swap">
<style>
  :root {
    --lavender: #dec8e3;
    --lavender-soft: #e6d4ea;
    --lavender-line: #d9c3df;
    --white: #ffffff;
    --pink: #d35fa6;
    --ink: #1c1c1c;
    --pastry-cream: #f7e39b;
    --pastry-gold: #e8bd45;
    --flourish: #3a3a3a;
  }
  html, body {
    margin: 0;
    padding: 0;
    width: 1200px;
    height: 686px;
    overflow: hidden;
    background: var(--white);
  }
  .card {
    position: relative;
    width: 1200px;
    height: 686px;
    background: var(--lavender);
    overflow: hidden;
  }
  .card-field {
    position: absolute;
    left: 0;
    top: 55px;
    width: 1200px;
    height: 592px;
    background: linear-gradient(180deg, var(--lavender-soft) 0%, var(--lavender) 100%);
  }
  .edge-teeth {
    position: absolute;
    left: 0;
    width: 1200px;
    background: repeating-linear-gradient(90deg,
      var(--white) 0, var(--white) 22px,
      var(--lavender) 22px, var(--lavender) 30px);
  }
  .edge-teeth--top { top: 0; height: 23px; }
  .edge-teeth--bottom { bottom: 0; height: 25px; }
  .edge-rule {
    position: absolute;
    left: 0;
    width: 1200px;
    background: var(--white);
  }
  .edge-rule--top { top: 43px; height: 12px; }
  .edge-rule--bottom { top: 647px; height: 11px; }
  .pastry-sketch {
    position: absolute;
    left: 114px;
    top: 114px;
    width: 377px;
    height: 412px;
    border-radius: 46% 46% 40% 40%;
    background: radial-gradient(ellipse at 50% 45%, var(--pastry-cream) 0%, var(--pastry-gold) 100%);
  }
  .label-ornament {
    position: absolute;
    left: 594px;
    top: 63px;
    width: 572px;
    height: 577px;
    border-radius: 42%;
    background: rgba(255, 255, 255, 0.5);
  }
  .label-plate {
    position: absolute;
    left: 611px;
    top: 200px;
    width: 543px;
    height: 303px;
    border-radius: 130px;
    background: var(--white);
  }
  .label-plate::after {
    content: "";
    position: absolute;
    inset: 10px;
    border: 2px solid var(--lavender-line);
    border-radius: 120px;
  }
  .brand-name {
    position: absolute;
    left: 639px;
    width: 500px;
    top: 238px;
    margin: 0;
    text-align: center;
    font-family: "Great Vibes", cursive;
    font-weight: 400;
    font-size: 84px;
    line-height: 1;
    color: var(--pink);
  }
  .brand-tagline {
    position: absolute;
    left: 619px;
    width: 540px;
    top: 332px;
    margin: 0;
    text-align: center;
    font-family: "Tinos", serif;
    font-weight: 400;
    font-size: 47px;
    line-height: 1;
    color: var(--ink);
  }
  .tagline-flourish {
    position: absolute;
    left: 777px;
    top: 400px;
    width: 200px;
    height: 38px;
  }
</style>
</head>
<body>
  <main class="card">
    <div class="card-field" role="img" aria-label="Soft lavender diamond pattern background"></div>
    <div class="edge-teeth edge-teeth--top"></div>
    <div class="edge-rule edge-rule--top"></div>

    <div class="pastry-sketch" role="img" aria-label="Sketch of a cream puff with chocolate glaze, whipped cream and a strawberry on top"></div>

    <div class="label-ornament" role="img" aria-label="White scrolled ornamental frame around the name label"></div>
    <div class="label-plate"></div>
    <h1 class="brand-name">Crumb Joy</h1>
    <p class="brand-tagline">BAKE GOODS &amp; MORE</p>
    <svg class="tagline-flourish" viewBox="0 0 200 38" aria-hidden="true">
      <path d="M10 22 C40 6, 70 34, 100 20 C130 6, 160 34, 190 18" fill="none" stroke="var(--flourish)" stroke-width="3" stroke-linecap="round"/>
    </svg>

    <div class="edge-rule edge-rule--bottom"></div>
    <div class="edge-teeth edge-teeth--bottom"></div>
  </main>
</body>
</html>
```